Corvin Mechanical Services
Your Complete Heating & Cooling Solution
Professional
Tomas Brenner
P.O. Box 7142
Baltimore, MD 21794
tomas@corvinms-example.com
www.corvinms-example.com
Licensed and Insured
Open for any ideas

```html
<!DOCTYPE html>
<html lang="en">
<head>
<meta charset="utf-8">
<title>Corvin Mechanical Services – Stationery</title>
<link href="https://fonts.googleapis.com/css2?family=Open+Sans:wght@400;600;700&display=swap" rel="stylesheet">
<style>
:root{
  --board:#2b2b2d;
  --board-line:#333336;
  --paper:#ffffff;
  --ink:#2a2a2a;
  --muted:#8a8a8a;
  --green:#8cc63f;
  --green-dark:#5f9e1f;
  --blue:#1b5fbf;
  --blue-dark:#0d3a86;
  --caption:#9a9a9a;
  --faint:#eef1f4;
}
*{box-sizing:border-box;margin:0;padding:0}
html,body{width:1200px;height:437px;overflow:hidden}
body{
  background:var(--board) repeating-linear-gradient(45deg,var(--board) 0 6px,var(--board-line) 6px 7px);
  font-family:"Open Sans",Arial,sans-serif;color:var(--ink);position:relative;
}
.piece{position:absolute;background:var(--paper);box-shadow:0 2px 6px rgba(0,0,0,.5);overflow:hidden}
.wrap{position:absolute}
.wrap > .piece{position:relative}
.caption{position:absolute;left:0;right:0;top:100%;margin-top:4px;font-size:7px;line-height:1;color:var(--caption);text-align:center;white-space:nowrap}

.brand{display:flex;align-items:center;gap:5px}
.brand-dot{border-radius:50%;background:var(--blue);flex:none}
.brand-name{font-weight:700;color:var(--blue-dark);line-height:1}
.tagline{font-size:5px;color:var(--muted);white-space:nowrap}

.faint-mark{position:absolute;border-radius:50%;background:var(--faint)}
.band{position:absolute;left:0;right:0;height:5px;background:linear-gradient(90deg,var(--green),var(--blue))}

/* business cards */
.card{width:139px;height:84px}
.card .brand{position:absolute;left:10px;top:14px}
.card .brand-dot{width:16px;height:16px}
.card .brand-name{font-size:17px}
.card .tagline{position:absolute;left:10px;top:33px}
.card .person{position:absolute;left:10px;bottom:14px;font-size:5px;line-height:1.4}
.card .person b{color:var(--blue-dark);font-size:6px}
.card .contact{position:absolute;right:8px;bottom:14px;font-size:4.5px;line-height:1.5;text-align:right;color:#555;white-space:nowrap}
.card.back{background:linear-gradient(160deg,var(--blue),var(--blue-dark))}
.card.back .center-dot{position:absolute;left:50%;top:50%;width:30px;height:30px;margin:-19px 0 0 -15px;border-radius:50%;border:3px solid #fff}
.card.back .web{position:absolute;bottom:8px;width:100%;text-align:center;font-size:5px;color:#fff}

/* letterheads */
.letter{width:312px;height:331px}
.letter .brand{position:absolute;left:20px;top:14px}
.letter .brand-dot{width:16px;height:16px}
.letter .brand-name{font-size:20px}
.letter .tagline{position:absolute;left:20px;top:34px}
.letter .contact{position:absolute;right:22px;top:14px;font-size:4.5px;line-height:1.6;color:#555;white-space:nowrap}
.letter .footer{position:absolute;bottom:12px;width:100%;text-align:center;font-size:4.5px;color:#666;white-space:nowrap}
.letter.centered .brand{left:50%;transform:translateX(-50%)}
.letter.centered .tagline{left:0;width:100%;text-align:center}

/* envelopes */
.env{width:331px;height:80px}
.env .flap{position:absolute;inset:0}
.env .brand{position:absolute;left:14px;top:14px}
.env .brand-dot{width:14px;height:14px}
.env .brand-name{font-size:17px}
.env .tagline{position:absolute;left:14px;top:32px}
</style>
</head>
<body>

<!-- business cards -->
<div class="wrap" style="left:24px;top:70px">
  <div class="piece card">
    <div class="brand"><span class="brand-dot"></span><span class="brand-name">Corvin</span></div>
    <div class="tagline">Your Complete Heating &amp; Cooling Solution</div>
    <div class="person"><b>Tomas Brenner</b><br>Professional</div>
    <div class="contact">410-555-0142<br>tomas@corvinms-example.com<br>www.corvinms-example.com</div>
    <div class="band" style="bottom:0;height:4px"></div>
  </div>
  <div class="caption">Front Card</div>
</div>

<div class="wrap" style="left:24px;top:170px">
  <div class="piece card back">
    <span class="center-dot"></span>
    <div class="web">www.corvinms-example.com</div>
  </div>
  <div class="caption">Back Card Option</div>
</div>

<div class="wrap" style="left:24px;top:270px">
  <div class="piece card">
    <div class="faint-mark" style="right:-14px;top:-8px;width:70px;height:70px"></div>
    <div class="brand"><span class="brand-dot"></span><span class="brand-name">Corvin</span></div>
    <div class="tagline">Your Complete Heating &amp; Cooling Solution</div>
    <div class="person"><b>Tomas Brenner</b><br>Licensed and Insured</div>
    <div class="band" style="bottom:0;height:4px"></div>
  </div>
  <div class="caption">Alternative Front Card</div>
</div>

<!-- letterheads -->
<div class="wrap" style="left:175px;top:29px">
  <div class="piece letter">
    <div class="brand"><span class="brand-dot"></span><span class="brand-name">Corvin</span></div>
    <div class="tagline">Your Complete Heating &amp; Cooling Solution</div>
    <div class="contact">Tel 410-555-0142<br>Fax 410-555-0143<br>tomas@corvinms-example.com<br>www.corvinms-example.com</div>
    <div class="faint-mark" style="left:86px;top:100px;width:140px;height:140px"></div>
    <div class="footer">P.O. Box 7142 &nbsp;·&nbsp; Baltimore, MD 21794</div>
    <div class="band" style="bottom:0"></div>
  </div>
  <div class="caption">Letterhead Option 01</div>
</div>

<div class="wrap" style="left:509px;top:29px">
  <div class="piece letter centered">
    <div class="brand"><span class="brand-dot"></span><span class="brand-name">Corvin</span></div>
    <div class="tagline">Your Complete Heating &amp; Cooling Solution</div>
    <div class="faint-mark" style="left:86px;top:100px;width:140px;height:140px"></div>
    <div class="footer">P.O. Box 7142 · Baltimore, MD 21794 · 410-555-0142 · www.corvinms-example.com</div>
    <div class="band" style="bottom:0"></div>
  </div>
  <div class="caption">Letterhead Option 02</div>
</div>

<!-- envelopes -->
<div class="piece env" style="left:845px;top:29px">
  <svg class="flap" viewBox="0 0 331 80" preserveAspectRatio="none">
    <defs><linearGradient id="g1" x1="0" y1="0" x2="0" y2="1"><stop offset="0" stop-color="#8cc63f"/><stop offset="1" stop-color="#5f9e1f"/></linearGradient></defs>
    <rect width="331" height="80" fill="#f4f4f4"/>
    <path d="M0 0H331V34L165 62L0 34Z" fill="url(#g1)"/>
    <circle cx="165" cy="24" r="8" fill="#1b5fbf"/>
  </svg>
</div>

<div class="piece env" style="left:845px;top:113px">
  <svg class="flap" viewBox="0 0 331 80" preserveAspectRatio="none">
    <defs><linearGradient id="g2" x1="0" y1="0" x2="0" y2="1"><stop offset="0" stop-color="#0d3a86"/><stop offset="1" stop-color="#1b5fbf"/></linearGradient></defs>
    <rect width="331" height="80" fill="#f4f4f4"/>
    <path d="M0 0H331V34L165 62L0 34Z" fill="url(#g2)"/>
    <circle cx="165" cy="24" r="8" fill="#8cc63f"/>
  </svg>
</div>

<div class="piece env" style="left:845px;top:187px;height:77px">
  <svg class="flap" viewBox="0 0 331 77" preserveAspectRatio="none">
    <rect width="331" height="77" fill="#fafafa"/>
    <path d="M0 0L165 44L331 0" fill="none" stroke="#d8d8d8" stroke-width="1"/>
    <path d="M0 77L140 38M331 77L190 38" fill="none" stroke="#e2e2e2" stroke-width="1"/>
  </svg>
</div>

<div class="wrap" style="left:845px;top:264px">
  <div class="piece env" style="height:96px">
    <div class="brand"><span class="brand-dot"></span><span class="brand-name">Corvin</span></div>
    <div class="tagline">Your Complete Heating &amp; Cooling Solution</div>
    <div class="faint-mark" style="right:30px;top:10px;width:70px;height:70px"></div>
    <div class="band" style="bottom:0;height:4px"></div>
  </div>
  <div class="caption">Envelope Front &amp; Back</div>
</div>

</body>
</html>
```